Flyer Design Project

Lanterns of Yore is a new collaborative of non-profit historical sites in the Greater Boston area. We're promoting the soft launch of our website by hosting open houses at each of the sites on September 21. We need a flyer to post up at each of the sites.

I have more print design needs to follow, and would really like to have a consistent look, so I intend to directly invite the winning designer to more projects.

Industry/Entity Type

Non-Profit

Requirements
Must have
• The flyer must be one page and be delivered as two files in Microsoft Publisher OR Microsoft Word. One file is for an 8 1/2 x 11 and one is as an 11 x 17 (same design, just scaled larger to fit the bigger paper).

It must have the Lanterns of Yore Logo (attached), and this text (attached) and use black font.

Any color that is not black or white must be chosen from these colors-but don't feel you have to use all of them:

Lanterns of Yore Website Colors

poppy red
c 0
m 93
y 87
k 0
web FF3333

nectarine
c 0
m 54
y 74
k 0
web FF9966

monaco blue

c 100
m 79
y 28
k 12
web 003366

tender shoots
c 30
m 0
y 89
k 0
web CCCC33

emerald
c 80
m 11
y 56
k 0
web 009999

african violet
c 28
m 44
y 0
k 0

web CC99CC

sunflower
c 10
m 33
y 99
k 0
web FF9933

lemon zest
c 4
m 13
y 77
k 0
web FFCC66

Nice to have
• Text and images with in the flyer should be large, simple and clear-as easy to see and read when the entire flyer is viewed on a mobile phone or from a distance as possible.

```html
<!DOCTYPE html>
<html lang="en">
<head>
<meta charset="utf-8">
<title>Lanterns of Yore – Open House Flyer</title>
<link rel="stylesheet" href="https://fonts.googleapis.com/css2?family=Anton&family=Oswald:wght@500;600;700&family=Open+Sans:wght@400;600&display=swap">
<style>
  :root {
    --poppy: #ff3333;
    --poppy-dark: #b51f1f;
    --monaco: #003366;
    --shoots: #c4d236;
    --emerald: #17a58f;
    --violet: #bb99cc;
    --sunflower: #ff9933;
    --lemon: #ffcc66;
    --ink: #111111;
    --body-text: #444444;
    --paper: #ffffff;
    --backdrop: #ecebe8;
  }
  * { box-sizing: border-box; margin: 0; padding: 0; }
  html, body { width: 988px; height: 1200px; overflow: hidden; background: var(--backdrop); }
  .flyer {
    position: absolute; left: 35px; top: 5px; width: 918px; height: 1190px;
    background: var(--paper); overflow: hidden;
    font-family: "Open Sans", Arial, sans-serif;
  }
  .abs { position: absolute; }

  .brand { left: 70px; top: 62px; display: flex; align-items: center; gap: 26px; }
  .brand-square { width: 96px; height: 96px; background: var(--violet); }
  .brand-name {
    font-family: "Oswald", Arial, sans-serif; font-weight: 500;
    color: var(--monaco); font-size: 64px; line-height: 1.02;
  }

  .date-day {
    left: 563px; top: 141px; width: 265px; height: 52px;
    background: var(--violet); border-radius: 6px 6px 0 0;
    font-family: "Oswald", Arial, sans-serif; font-weight: 700; color: #fff;
    font-size: 34px; text-align: center; line-height: 52px;
  }
  .date-ribbon { left: 520px; top: 186px; width: 355px; height: 74px; }
  .date-full {
    left: 543px; top: 190px; width: 309px; height: 64px;
    font-family: "Oswald", Arial, sans-serif; font-weight: 700; color: #fff;
    font-size: 38px; text-align: center; line-height: 64px;
  }

  .band { left: 0; top: 200px; width: 918px; height: 300px; }

  .topics { left: 45px; top: 290px; width: 840px; height: 190px; }
  .topic {
    position: absolute; display: flex; align-items: center; gap: 24px;
    font-family: "Anton", Impact, sans-serif; font-size: 50px; color: var(--ink);
    letter-spacing: 1px; line-height: 1;
  }
  .topic svg { width: 36px; height: 36px; flex: none; }

  .intro {
    left: 45px; top: 498px; width: 826px;
    font-size: 18.5px; line-height: 29px; color: var(--body-text); text-align: justify;
  }

  .cta-box {
    left: 92px; top: 636px; width: 346px; height: 122px; border-radius: 16px;
    background: var(--poppy); box-shadow: 0 5px 8px rgba(0,0,0,.35);
    color: #fff; text-align: center; padding-top: 16px;
    font-family: "Oswald", Arial, sans-serif;
  }
  .cta-lead { font-size: 21px; font-weight: 500; line-height: 28px; }
  .cta-url { font-size: 31px; font-weight: 600; line-height: 44px; }

  .callout {
    left: 92px; top: 804px; width: 346px; height: 132px; border-radius: 16px;
    background: var(--emerald); box-shadow: 0 5px 8px rgba(0,0,0,.35);
    text-align: center; padding-top: 8px;
    font-family: "Oswald", Arial, sans-serif; color: #fff; font-size: 30px; font-weight: 600;
  }
  .callout-field {
    margin: 6px auto 0; width: 308px; height: 62px; border-radius: 10px; background: #f2f2f2;
  }

  .highlights {
    left: 92px; top: 970px; width: 346px; text-align: center;
    font-family: "Oswald", Arial, sans-serif; font-weight: 700; color: var(--monaco);
    font-size: 40px; line-height: 56px;
  }

  .orgs-title {
    left: 482px; top: 622px; width: 400px;
    font-family: "Oswald", Arial, sans-serif; font-weight: 600; color: var(--monaco);
    font-size: 22px; line-height: 29px;
  }
  .orgs { left: 482px; top: 740px; width: 410px; list-style: none; }
  .orgs li {
    display: flex; gap: 12px; font-size: 14px; line-height: 21px; color: #333;
    margin-bottom: 6px; font-family: "Oswald", Arial, sans-serif; font-weight: 500;
  }
  .orgs svg { width: 14px; height: 14px; flex: none; margin-top: 4px; }

  .stripes { left: 0; bottom: 0; width: 918px; height: 32px; }
</style>
</head>
<body>
<main class="flyer">
  <div class="abs brand">
    <div class="brand-square"></div>
    <div class="brand-name">Lanterns of<br>Yore</div>
  </div>

  <svg class="abs band" viewBox="0 0 918 300" aria-hidden="true">
    <polygon fill="var(--shoots)" points="0,40 250,40 276,8 918,8 918,278 895,262 640,262 615,290 0,290"/>
  </svg>

  <div class="abs date-day">SATURDAY</div>
  <svg class="abs date-ribbon" viewBox="0 0 355 74" aria-hidden="true">
    <polygon fill="var(--poppy-dark)" points="0,10 28,10 28,50 10,50 20,30"/>
    <polygon fill="var(--poppy-dark)" points="355,10 327,10 327,50 345,50 335,30"/>
    <rect x="23" y="4" width="309" height="64" rx="6" fill="var(--poppy)"/>
  </svg>
  <div class="abs date-full">SEPTEMBER 21</div>

  <div class="abs topics">
    <div class="topic" style="left:0;top:0"><svg viewBox="0 0 36 36"><rect x="2" y="6" width="28" height="28" fill="#fff" stroke="var(--ink)" stroke-width="3"/><path d="M8 20 l7 8 L33 4" fill="none" stroke="var(--poppy)" stroke-width="5"/></svg>COLUMBUS</div>
    <div class="topic" style="left:386px;top:0"><svg viewBox="0 0 36 36"><rect x="2" y="6" width="28" height="28" fill="#fff" stroke="var(--ink)" stroke-width="3"/><path d="M8 20 l7 8 L33 4" fill="none" stroke="var(--poppy)" stroke-width="5"/></svg>PILGRIMS</div>
    <div class="topic" style="left:0;top:63px"><svg viewBox="0 0 36 36"><rect x="2" y="6" width="28" height="28" fill="#fff" stroke="var(--ink)" stroke-width="3"/><path d="M8 20 l7 8 L33 4" fill="none" stroke="var(--poppy)" stroke-width="5"/></svg>REVOLUTION</div>
    <div class="topic" style="left:386px;top:63px"><svg viewBox="0 0 36 36"><rect x="2" y="6" width="28" height="28" fill="#fff" stroke="var(--ink)" stroke-width="3"/><path d="M8 20 l7 8 L33 4" fill="none" stroke="var(--poppy)" stroke-width="5"/></svg>CIVIL WAR</div>
    <div class="topic" style="left:0;top:126px"><svg viewBox="0 0 36 36"><rect x="2" y="6" width="28" height="28" fill="#fff" stroke="var(--ink)" stroke-width="3"/><path d="M8 20 l7 8 L33 4" fill="none" stroke="var(--poppy)" stroke-width="5"/></svg>INDUSTRIALIZATION</div>
  </div>

  <p class="abs intro">You know the history. But do you know the stories? Have you found how YOU are connected to the places and lives of the people who've shaped our world, our country, our state, and your life today? Find out by exploring some of Massachusetts' treasured historical gems - you'll be surprised by the wealth you discover.</p>

  <div class="abs cta-box">
    <div class="cta-lead">For hours, directions, and<br>discount/prize passes learn more at</div>
    <div class="cta-url">www.lanternsofyore.org</div>
  </div>

  <div class="abs callout">
    Call Out Box:
    <div class="callout-field"></div>
  </div>

  <div class="abs highlights">Special Tours,<br>Games, Prizes, and<br>Children's Activities!</div>

  <h2 class="abs orgs-title">Participating Organizations (must appear exactly as printed in the order listed)</h2>
  <ul class="abs orgs">
    <li><svg viewBox="0 0 14 14"><path d="M1 7 l4 5 L13 1" fill="none" stroke="var(--poppy)" stroke-width="3"/></svg>Harbor Hill at Wren Estate</li>
    <li><svg viewBox="0 0 14 14"><path d="M1 7 l4 5 L13 1" fill="none" stroke="var(--poppy)" stroke-width="3"/></svg>"Meeting House of the Founders" First Parish (Unitarian) of Easton</li>
    <li><svg viewBox="0 0 14 14"><path d="M1 7 l4 5 L13 1" fill="none" stroke="var(--poppy)" stroke-width="3"/></svg>Ashgrove Memorial Library</li>
    <li><svg viewBox="0 0 14 14"><path d="M1 7 l4 5 L13 1" fill="none" stroke="var(--poppy)" stroke-width="3"/></svg>Marlow Dance Theatre's Home at Old Fairhaven Baptist Church</li>
    <li><svg viewBox="0 0 14 14"><path d="M1 7 l4 5 L13 1" fill="none" stroke="var(--poppy)" stroke-width="3"/></svg>Kestrel's Boat Shop and Museum</li>
    <li><svg viewBox="0 0 14 14"><path d="M1 7 l4 5 L13 1" fill="none" stroke="var(--poppy)" stroke-width="3"/></svg>Mount Linden Cemetery</li>
    <li><svg viewBox="0 0 14 14"><path d="M1 7 l4 5 L13 1" fill="none" stroke="var(--poppy)" stroke-width="3"/></svg>Museum of Coastal Heritage: Harbor Campus</li>
    <li><svg viewBox="0 0 14 14"><path d="M1 7 l4 5 L13 1" fill="none" stroke="var(--poppy)" stroke-width="3"/></svg>Museum of Coastal Heritage: Island Campus</li>
    <li><svg viewBox="0 0 14 14"><path d="M1 7 l4 5 L13 1" fill="none" stroke="var(--poppy)" stroke-width="3"/></svg>Memorial to the Early Settlers</li>
    <li><svg viewBox="0 0 14 14"><path d="M1 7 l4 5 L13 1" fill="none" stroke="var(--poppy)" stroke-width="3"/></svg>Old Stone Meeting House</li>
    <li><svg viewBox="0 0 14 14"><path d="M1 7 l4 5 L13 1" fill="none" stroke="var(--poppy)" stroke-width="3"/></svg>The Briar Park Carousel</li>
    <li><svg viewBox="0 0 14 14"><path d="M1 7 l4 5 L13 1" fill="none" stroke="var(--poppy)" stroke-width="3"/></svg>Thomas Avery House</li>
    <li><svg viewBox="0 0 14 14"><path d="M1 7 l4 5 L13 1" fill="none" stroke="var(--poppy)" stroke-width="3"/></svg>The Elm Street Shul, Center for Local Culture</li>
  </ul>

  <svg class="abs stripes" viewBox="0 0 918 32" aria-hidden="true">
    <g fill="var(--lemon)">
      <rect x="8" y="0" width="12" height="32"/><rect x="78" y="0" width="12" height="32"/><rect x="215" y="0" width="12" height="32"/><rect x="290" y="0" width="12" height="32"/><rect x="368" y="0" width="12" height="32"/><rect x="470" y="0" width="12" height="32"/><rect x="505" y="0" width="12" height="32"/><rect x="632" y="0" width="12" height="32"/><rect x="740" y="0" width="12" height="32"/><rect x="835" y="0" width="12" height="32"/>
    </g>
    <g fill="var(--violet)">
      <rect x="40" y="0" width="12" height="32"/><rect x="130" y="0" width="12" height="32"/><rect x="180" y="0" width="12" height="32"/><rect x="330" y="0" width="12" height="32"/><rect x="430" y="0" width="12" height="32"/><rect x="545" y="0" width="12" height="32"/><rect x="600" y="0" width="12" height="32"/><rect x="668" y="0" width="12" height="32"/><rect x="705" y="0" width="12" height="32"/><rect x="780" y="0" width="12" height="32"/><rect x="870" y="0" width="12" height="32"/><rect x="905" y="0" width="12" height="32"/>
    </g>
    <g fill="var(--poppy)">
      <rect x="392" y="0" width="12" height="32"/><rect x="450" y="0" width="12" height="32"/><rect x="520" y="0" width="12" height="32"/><rect x="575" y="0" width="12" height="32"/>
    </g>
  </svg>
</main>
</body>
</html>
```